Business Card for supplement company

Company Name: Pinevale Nutrition
We require quite a simple yet stand out business card for our supplement company.
We are selling high end bodybuilding supplements direct to the public through online sales and Facebook marketing.
There will be slightly varying versions of the card and the winning design will be required to make these slight adjustments.
We will also require the file to be provided in and editable version as we will have a discount code on there that will be changed for different people.
Employee Cards:
Logo on the front of the card (see attached EPS file)
Please also add slogan in text "When Failure is Not and Option" as close as possible to what is seen in this link www.pinevalenutrition.com.au
Suggestions: Card in black, possibly use a similar background to website theme (honeycomb, carbon look)
Information to be included on the back (please place and order accordingly)
:Clive Marrowby (Director)
Email: clive@pinevalenutrition.com.au
Phone: 02 5918 2273
Website: www.pinevalenutrition.com.au
Athlete Cards:
Front:
Same as above
Back:
Discount Code: xxx123 (to be editable)
Facebook: www.facebook.com/PinevaleNutrition
Design ideas: please look at our website and facebook signup page for design ideas.

```html
<!DOCTYPE html>
<html lang="en">
<head>
<meta charset="utf-8">
<title>Pinevale Nutrition – Business Card</title>
<link href="https://fonts.googleapis.com/css2?family=Didact+Gothic&display=swap" rel="stylesheet">
<style>
  :root {
    --page-bg: #6d6d6b;
    --card-black: #0d0e0d;
    --card-dark: #1c1e1c;
    --neon-green: #1ee61e;
    --deep-green: #0aa80a;
    --slogan-orange: #e2961c;
    --accent-orange: #ff6a1a;
    --text-white: #f2f2f2;
    --text-grey: #6a6a6a;
    --strip-grey: rgba(255,255,255,0.07);
  }
  * { box-sizing: border-box; margin: 0; padding: 0; }
  html, body {
    width: 1200px; height: 944px; overflow: hidden;
    background: var(--page-bg);
    font-family: "Didact Gothic", "Century Gothic", sans-serif;
  }
  .canvas { position: relative; width: 1200px; height: 944px; }
  .card {
    position: absolute; left: 232px; width: 736px; height: 420px;
    overflow: hidden; border-radius: 3px;
    box-shadow: 0 10px 30px rgba(0,0,0,0.45);
  }
  .card--front { top: 36px; }
  .card--back { top: 488px; }
  .card__texture {
    position: absolute; inset: 0;
    background: radial-gradient(ellipse at 55% 45%, var(--card-dark) 0%, var(--card-black) 75%);
  }
  .green-band {
    position: absolute; top: 0; bottom: 0; width: 96px;
    background: linear-gradient(90deg, var(--deep-green), var(--neon-green) 45%, var(--neon-green) 60%, var(--deep-green));
    box-shadow: 0 0 22px rgba(30,230,30,0.55);
  }
  .card--front .green-band { left: 110px; }
  .card--back .green-band { left: 462px; }

  .brand {
    position: absolute; left: 300px; top: 128px; width: 400px; text-align: center;
  }
  .brand__name {
    color: var(--neon-green); font-size: 46px; letter-spacing: 1px; line-height: 1.1;
  }
  .brand__slogan {
    margin-top: 18px; color: var(--slogan-orange); font-size: 19px; letter-spacing: 0.5px;
  }

  .holder { position: absolute; left: 52px; top: 64px; }
  .holder__name {
    color: var(--text-white); font-size: 44px; letter-spacing: 0.5px;
    text-shadow: 0 0 4px var(--neon-green), 0 0 10px rgba(30,230,30,0.6);
  }
  .holder__title { color: var(--text-grey); font-size: 18px; margin-left: 4px; }

  .contact-strip {
    position: absolute; left: 150px; right: 0; top: 292px; height: 96px;
    background: var(--strip-grey);
  }
  .contact {
    position: absolute; left: 36px; top: 286px;
    display: grid; grid-template-columns: 120px auto; row-gap: 8px;
    border-left: 4px solid var(--accent-orange); padding-left: 10px;
    font-size: 19px;
  }
  .contact__label { color: var(--neon-green); }
  .contact__value { color: var(--text-white); }
  .contact__value .hl { color: var(--neon-green); }
</style>
</head>
<body>
<main class="canvas">
  <section class="card card--front">
    <div class="card__texture" role="img" aria-label="Dark honeycomb carbon texture"></div>
    <div class="green-band"></div>
    <div class="brand">
      <div class="brand__name">Pinevale Nutrition</div>
      <div class="brand__slogan">Stronger when it matters most</div>
    </div>
  </section>

  <section class="card card--back">
    <div class="card__texture" role="img" aria-label="Dark honeycomb carbon texture"></div>
    <div class="contact-strip"></div>
    <div class="green-band"></div>
    <div class="holder">
      <div class="holder__name">Clive Marrowby</div>
      <div class="holder__title">Director</div>
    </div>
    <div class="contact">
      <span class="contact__label">Email:</span>
      <span class="contact__value">clive<span class="hl">@</span>pinevalenutrition.com.au</span>
      <span class="contact__label">Phone:</span>
      <span class="contact__value">02 5918 2273</span>
      <span class="contact__label">Website:</span>
      <span class="contact__value">www.<span class="hl">pinevalenutrition</span>.com.au</span>
    </div>
  </section>
</main>
</body>
</html>
```